Tax Preparation flyer for LedgerWise Corp.

My Client would like a one page PDF flyer to promote upcoming tax season in Canada. This firm is affordable and all virtual. I have attached a copy of their logo and a word document with the proposed wording for the flyer. Please feel free to change if you have better suggestions.

Target Market(s)

individuals in canada

Colors
0054AA
0677BA
7BADD7
CADEEF
E8F1F8

```html
<!DOCTYPE html>
<html lang="en">
<head>
<meta charset="utf-8">
<title>LedgerWise Corp. – Tax Season Flyer</title>
<link rel="stylesheet" href="https://fonts.googleapis.com/css2?family=Montserrat:wght@700;800&family=Arimo:wght@400;700&display=swap">
<style>
  :root {
    --sky: #1b93d5;
    --deep-blue: #0677ba;
    --charcoal: #3a3b3d;
    --ink: #3d3f44;
    --body-text: #4a4c52;
    --soft-grey: #d9dce1;
    --paper: #ffffff;
    --backdrop: #eeeeee;
  }
  * { box-sizing: border-box; margin: 0; padding: 0; }
  html, body { width: 1200px; height: 1200px; overflow: hidden; }
  body { background: var(--backdrop); font-family: "Arimo", Arial, sans-serif; }

  .flyer {
    position: absolute; left: 204px; top: 40px;
    width: 792px; height: 1120px;
    background: var(--paper);
    overflow: hidden;
  }
  .flyer-shapes { position: absolute; inset: 0; width: 792px; height: 1120px; }

  .brand {
    position: absolute; left: 36px; top: 24px; width: 180px;
    font-family: "Montserrat", sans-serif; font-weight: 700;
    color: var(--deep-blue); text-align: center;
  }
  .brand .name { display: block; font-size: 27px; line-height: 32px; }
  .brand .suffix { display: block; font-size: 22px; line-height: 26px; }

  .headline {
    position: absolute; left: 22px; top: 144px;
    font-family: "Montserrat", sans-serif; font-weight: 800;
    color: var(--paper); text-transform: uppercase;
  }
  .headline .lead { display: block; font-size: 62px; line-height: 62px; letter-spacing: 1px; }
  .headline .rest { display: block; font-size: 33px; line-height: 39px; margin-top: 4px; }

  .intro {
    position: absolute; left: 22px; top: 350px; width: 332px;
    font-weight: 700; font-size: 19px; line-height: 24.5px; color: var(--paper);
  }

  .pricing-title {
    position: absolute; right: 16px; top: 352px;
    font-weight: 700; font-size: 28px; color: var(--sky);
  }
  .price-main {
    position: absolute; left: 426px; top: 406px; width: 358px; height: 35px;
    background: var(--sky); color: var(--paper);
    font-weight: 700; font-size: 20px; line-height: 35px; text-align: center;
  }
  .price-extra {
    position: absolute; left: 430px; top: 450px; width: 354px;
    color: var(--paper); font-weight: 700; font-size: 17px; line-height: 21px; text-align: center;
  }
  .price-note {
    position: absolute; left: 442px; top: 502px; width: 330px;
    color: var(--soft-grey); font-size: 15px; line-height: 19px; text-align: center;
  }

  .about {
    position: absolute; left: 22px; top: 602px; width: 748px;
    font-weight: 700; font-size: 16px; line-height: 21px; color: var(--ink); text-align: justify;
  }
  .process {
    position: absolute; left: 22px; top: 706px; width: 748px;
    font-size: 16px; line-height: 21px; color: var(--body-text); text-align: justify;
  }
  .perks {
    position: absolute; left: 314px; top: 800px; width: 462px;
    list-style: none; font-size: 16px; line-height: 20px; color: var(--body-text);
  }
  .perks li { position: relative; padding-left: 18px; }
  .perks li::before {
    content: ""; position: absolute; left: 2px; top: 8px;
    width: 5px; height: 5px; border-radius: 50%; background: var(--sky);
  }

  .cta-title {
    position: absolute; right: 16px; top: 955px;
    font-weight: 700; font-size: 24px; color: var(--paper); letter-spacing: 0.3px;
  }
  .cta-line {
    position: absolute; left: 340px; top: 1006px; width: 440px;
    font-weight: 700; font-size: 25px; color: var(--paper); text-align: center;
  }
  .contact { position: absolute; left: 470px; top: 1040px; list-style: none; }
  .contact li {
    display: flex; align-items: center; gap: 10px;
    font-weight: 700; font-size: 18px; color: var(--paper); height: 24px; margin-bottom: 10px;
  }
  .contact svg { width: 22px; height: 22px; flex: none; }
</style>
</head>
<body>
<main class="flyer">
  <svg class="flyer-shapes" viewBox="206 100 566 800" preserveAspectRatio="none">
    <defs>
      <linearGradient id="office-tones" x1="0" y1="0" x2="1" y2="1">
        <stop offset="0" stop-color="#2d3a4c"/>
        <stop offset="0.55" stop-color="#5b6878"/>
        <stop offset="1" stop-color="#8a7560"/>
      </linearGradient>
      <linearGradient id="lounge-tones" x1="0" y1="0" x2="1" y2="1">
        <stop offset="0" stop-color="#d9dde2"/>
        <stop offset="0.6" stop-color="#b9bfc8"/>
        <stop offset="1" stop-color="#8f8a84"/>
      </linearGradient>
    </defs>

    <polygon class="hero-photo" role="img" aria-label="Photo: professional typing on a laptop with floating tax icons"
             fill="url(#office-tones)" points="372,100 772,100 772,347 500,347"/>
    <polygon class="hero-panel" fill="var(--sky)" points="206,170 408,170 510,360 432,512 206,512"/>
    <polygon class="pricing-panel" fill="var(--charcoal)" points="508,385 772,385 772,512 442,512"/>

    <polygon class="footer-band" fill="var(--sky)" points="345,712 368,712 418,808 772,808 772,900 445,900"/>
    <polygon class="cta-band" fill="var(--charcoal)" points="552,778 772,778 772,808 536,808"/>
    <polygon class="relax-photo" role="img" aria-label="Photo: relaxed man leaning back on a sofa"
             fill="url(#lounge-tones)" points="206,712 345,712 445,900 206,900"/>
  </svg>

  <div class="brand"><span class="name">LedgerWise</span><span class="suffix">Corp.</span></div>

  <h1 class="headline">
    <span class="lead">Relax</span>
    <span class="rest">We’ve got<br>your taxes<br>covered!</span>
  </h1>

  <p class="intro">Imagine having your bookkeeping on auto pilot, with everything always up to date and available at your fingertips. Anytime. Anywhere. You’ll always know exactly where you stand with your cash flow how much you have, owe, are owed, and have made.</p>

  <h2 class="pricing-title">PRICING</h2>
  <div class="price-main">PERSONAL TAX RETURN $100</div>
  <p class="price-extra">Add a business or rental schedule<br>$125 per business or rental property.</p>
  <p class="price-note">More complex tax returns will be assessed based on the complexity of the return and you will be advised before we start</p>

  <p class="about">Our tax preparers have over 20 years experience and worked both in public accounting firms as well as specialized tax. Our tax services are virtual, so you don’t have to take the time for a personal visit. We take care of everything and can access all your tax slips from the RevenueNet website directly into our tax software. All signing is done via SignFlow.</p>

  <p class="process">You can fill and submit the appropriate forms, along with all your other documents, in our secure client portal. It’s important that we understand your situation and any changes in your situation from the past year. If you have a complex tax situation and would like to discuss it, we can meet in virtually over MeetSpace or TalkHub</p>

  <ul class="perks">
    <li>Did you fall behind in filing your income tax? Save 20% when you file 3 or more years with us. We can do back to 2012 for filing of tax returns.</li>
    <li>If you expect a refund, the earlier you file the sooner you will receive your refund. Our average turn around time prior to April is a couple of days.</li>
  </ul>

  <h2 class="cta-title">CONTACT US TODAY</h2>
  <p class="cta-line">so you can start to breathe easy.</p>
  <ul class="contact">
    <li>
      <svg viewBox="0 0 22 22" aria-hidden="true"><circle cx="11" cy="11" r="11" fill="var(--charcoal)"/><rect x="5.5" y="7" width="11" height="8" rx="1" fill="none" stroke="#fff" stroke-width="1.5"/><path d="M5.5 7.5 11 11.5 16.5 7.5" fill="none" stroke="#fff" stroke-width="1.5"/></svg>
      hello@ledgerwise.ca
    </li>
    <li>
      <svg viewBox="0 0 22 22" aria-hidden="true"><circle cx="11" cy="11" r="11" fill="var(--charcoal)"/><path d="M7.5 5.5c.6-.4 1.3-.3 1.6.3l1 1.8c.3.5.1 1.1-.3 1.4l-.8.6c.5 1.2 1.5 2.2 2.7 2.7l.6-.8c.3-.4.9-.6 1.4-.3l1.8 1c.6.3.7 1 .3 1.6l-.7.9c-.6.7-1.6.9-2.5.5-2.6-1.1-4.600-3.1-5.7-5.7-.4-.9-.2-1.900.5-2.5z" fill="#fff"/></svg>
      555 010 2468
    </li>
  </ul>
</main>
</body>
</html>
```